Drift Us to Haven.co.nz .... Tourism business providing guided tours.

Design and build a website for our new company. The company is one where we take tourists to beautiful places for a fully guided tour for 2 weeks. Tours can follow our itinerary or be tailored to suit individual clients. .... Let us tell you a little of what we are about ....
Flying our clients to paradise for a ‘ Tailor Made ‘ tour or one where we organise everything and use our combined knowledge of more than 50 years experience in Indonesia where we travel to some of the places that are not well known on the tourist map, places that are often off the beaten track of tourists but that are spectacularly beautiful.
Our team .... Marcus Thornbury (Ex Iron Fern), Garrick Pellow, Sekar Pellow & Ratna Wulansari have reached a stage in life where making money is not essential but enjoying life is. We all have a passion to help others experience what we have when we travel to our paradise whether that is Indonesia, where we are starting our tours then we will be working on Thailand, Malaysia, Vietnam or New Zealand along with a number of other countries.
The experience of the ‘ Ladies ‘ in the team who are both native to the country along with my experience in the Film Production business where I have produced a number of documentaries on travelling through Indonesia and show casing the spectacular scenery there gives our clients access to what they will experience through my You Tube channel. …. https://www.vidstreamo.example/user/dpellowfilm/videos
We claim to be the only tour company that produces documentaries on what our guests can expect to experience on their travels with us. All trips are personally guided with one of our team and we can also Taylor make trips where groups can be personally guided by the Ex Iron Fern in our team Marcus Thornbury. Further to that we film and produce a Video of your trip as it happens ... that is something special that you get to keep and show friends & family.
To top that off we have Marcus Thornbury on board who can call on his experience of travelling with the Iron Fern team but also his position as entertainment director for the IF’S on tour.
Marcus also has a vast experience as a host where he has hosted celebrities and entertained large companies which included Corvane the French aircraft maker and Kestrel Digest in Bali.
He has also been involved with organising events and hosting guests for the Prince and Princess of Monaco.
Ratna has a Batchelor degree in marketing and management and worked in the hotel industry and also runs Lodgora villas where she is working on expanding that to the next level in Bali.
By chance we had been working on forming such a tour company individually and when we all realised this it was obvious we needed to form a company where we can call on our individual strengths.
The company will soon introduce other celebrity guides for our tours that will open opportunities for other ex players of International teams that are looking for opportunities when their playing careers finish.
What really stands out in Indonesia is the people - we consider they are the friendliest of all the countries we have travelled through. As a film maker I experience this throughout the country. When I intrude on peoples life and culture I am invariably met with a response that is so touching. The people of Indonesia are so proud of their way of life and equally as proud that I show such interest in their life. Our target market is clients that want to experience what we want to experience.
Bali is one part of our trip but the Island of Bali and the 17,200 other islands that make up the Indonesian Archipelago are what we have so much experience in travelling thru (some of - not all .... Yet?) and that is what makes our paradise the aim of the tours.
The company is currently being formed along with our Logo, brochures and a comprehensive website that will be online in a couple of weeks. Further to that and what in fact will be the main promotional tool for our company, we have a number of documentaries that will showcase ‘ Radiant Isles ‘ from the air and the ground that have been produced and are under production by our own in-house Film production company Greenharbour films.
Links :https://www.vidstreamo.example/watch?v=Qx7pLm2TzRa&feature=vs.be&ref=Kd93hTpWmz0eLqRvXcYbNa51GsUjHwPoIfEkZt&app=desktop
Our contact details :
‘ Drift us to Haven ‘ driftustohavennz@mailbay.example
Garrick & Sekar Pellow oakbarn_goods@netlink.example
Marcus Thornbury: mthornbury17@mailbay.example

Target Market(s)

Older people with money to spend on holidays in Paradise .... We are adamant, at this stage that we are looking at the higher end of the market so that our tours are unique and not a crowded tour where all follow the leader. We want to retain the flexibility so that at the start of each day we can offer alternatives to what is on the itinerary. For example some of the group could go rafting and the ladies may prefer to go in another direction and to facilitate this we will have more than one vehicle on hand to do this.

Industry/Entity Type

Tourism

Coding

Coded - Design and coding required

Number of Pages Required

5+ page

Font styles to use
Serif

Colors
0792cd
85cae6
00a990

Requirements
Must have
• Buttons so prospective clients can book and pay for a trip
• Links to various Documentaries we have on out You Tube Page .... Greenharbour Films
• Contact details for each of the partners
Nice to have
• A similar site to https://www.lotuspathjourneys.example/premium-tours/

```html
<!DOCTYPE html>
<html lang="en">
<head>
<meta charset="utf-8">
<title>Drift Us to Haven</title>
<link href="https://fonts.googleapis.com/css2?family=Montserrat:ital,wght@0,400;0,500;0,600;0,700;0,800;1,400&display=swap" rel="stylesheet">
<style>
:root{
  --blue:#0792cd;
  --sky:#85cae6;
  --teal:#00a990;
  --ink:#2b2b2b;
  --text:#6b6b6b;
  --line:#e3e3e3;
  --panel:#f4f4f4;
  --ghost:#eef0f2;
  --white:#ffffff;
}
*{box-sizing:border-box;margin:0;padding:0}
html,body{width:1200px;height:4580px;overflow:hidden;background:var(--white)}
body{font-family:"Montserrat",Arial,sans-serif;color:var(--text)}
.page{position:relative;width:1200px;height:4580px;overflow:hidden}
.abs{position:absolute}

/* header */
.brand-panel{left:0;top:0;width:366px;height:739px;background:var(--blue)}
.brand{left:76px;top:40px;display:flex;align-items:center;gap:10px;color:var(--white);font-weight:700;font-size:17px;letter-spacing:.5px}
.brand-dot{width:16px;height:16px;border-radius:50%;background:var(--white)}
.util-nav{top:22px;right:80px;display:flex;gap:28px;font-size:15px;font-weight:600;color:var(--teal)}
.util-nav span{border-bottom:2px solid var(--teal);padding-bottom:3px}
.util-nav .sep{border:none;color:#bbb}
.main-nav{top:62px;left:440px;display:flex;gap:30px;font-size:13px;font-weight:500;color:#555}
.main-nav .active{color:var(--teal);border-top:2px solid var(--teal);padding-top:4px;margin-top:-6px}

/* hero */
.hero-photo{left:0;top:116px;width:1200px;height:525px;background:linear-gradient(120deg,#1f5d64 0%,#2f8d86 35%,#d9d3b8 52%,#2a7b7c 62%,#0f3f48 100%)}
.hero-title{left:76px;top:300px;color:var(--white);font-size:62px;font-weight:700;letter-spacing:2px;line-height:1}
.hero-sub{left:80px;top:380px;color:var(--white);font-size:30px;font-weight:600;letter-spacing:6px;line-height:1}
.hero-arrows{left:158px;top:610px;display:flex;gap:16px}
.hero-arrow{width:50px;height:50px;background:var(--white);display:flex;align-items:center;justify-content:center}
.video-disc{left:779px;top:489px;width:304px;height:304px;border-radius:50%;border:4px solid var(--white);background:radial-gradient(circle at 50% 55%,#2c7f83 0%,#174e57 60%,#0d3038 100%);overflow:hidden}
.video-label{position:absolute;top:72px;width:100%;text-align:center;color:var(--white);font-size:13px;font-weight:600;letter-spacing:.5px}
.play{position:absolute;left:118px;top:118px;width:66px;height:66px;border-radius:50%;background:var(--teal);display:flex;align-items:center;justify-content:center}

/* welcome */
.welcome-title{left:80px;top:880px;color:var(--blue);font-size:36px;font-weight:700;line-height:1.25}
.welcome-lede{left:80px;top:982px;width:480px;font-size:15px;font-style:italic;line-height:1.6;color:#777}
.welcome-body{left:626px;top:880px;width:494px;font-size:13.5px;line-height:1.7;color:#777}
.welcome-body p+p{margin-top:16px}

/* section titles */
.section-title{color:var(--blue);font-weight:700;text-align:center;width:1200px;left:0}
.ghost-word{color:var(--ghost);font-weight:800;letter-spacing:3px}

/* included */
.inc-title{top:1198px;font-size:27px}
.inc-ghost{left:76px;top:1212px;font-size:80px}
.inc-band{left:0;top:1265px;width:137px;height:350px;background:#e8f3fa}
.inc-list{left:76px;top:1312px;list-style:none;font-size:13px;color:#555}
.inc-list li{display:flex;align-items:flex-start;gap:14px;line-height:1.45;margin-bottom:16px;width:480px}
.inc-list li span{max-width:420px}
.inc-photo{left:632px;top:1282px;width:488px;height:312px;background:radial-gradient(ellipse at 40% 30%,#cfe6d4 0%,#3a8c8e 25%,#1e6b86 55%,#124a66 100%)}

/* tours */
.tours-title{top:1716px;font-size:38px}
.tours-ghost{left:830px;top:1712px;font-size:80px}
.tour-card{width:320px;height:626px;border:1px solid var(--line);background:var(--white)}
.tour-photo{height:229px}
.tour-meta{background:var(--panel);padding:26px 22px 20px}
.tour-name{font-size:16px;color:#666;padding-bottom:18px;border-bottom:1px solid #d6d6d6}
.tour-facts{display:flex;justify-content:space-between;margin-top:14px}
.tour-days{color:var(--teal);font-size:26px;font-weight:500;line-height:1}
.tour-days small,.tour-price small{display:block;font-size:11px;color:var(--teal);margin-top:4px;font-weight:500}
.tour-price{text-align:left;color:var(--teal);font-size:30px;font-weight:700;line-height:1}
.tour-price small{margin:0 0 3px}
.tour-text{padding:26px 22px 0;font-size:13.5px;line-height:1.6;color:#777}
.btn{display:inline-flex;align-items:center;justify-content:center;background:var(--teal);color:var(--white);font-weight:600;font-size:14px;letter-spacing:.5px}
.tour-btn{margin:24px 0 0 22px;width:148px;height:46px}
.explore-btn{left:497px;top:3145px;width:206px;height:50px;font-size:16px}

/* countries */
.countries-title{top:3300px;font-size:38px}
.countries-ghost{left:608px;top:3296px;font-size:80px}
.tile{display:flex;align-items:center;justify-content:center;color:var(--white);font-weight:600;text-shadow:0 1px 4px rgba(0,0,0,.35)}

/* footer */
.footer-rule{left:76px;top:4158px;width:1044px;height:1px;background:var(--line)}
.foot-col{top:4214px;list-style:none;font-size:13px;color:#666}
.foot-col li{height:38px}
.brochures{left:720px;top:4213px;display:flex;gap:26px}
.brochure{width:82px;height:116px;border:4px solid #1d1d1d;background:linear-gradient(180deg,#6b2430,#c04a5a 60%,#2a1418)}
.brochure-btn{left:790px;top:4360px;width:272px;height:46px;font-size:14px}
.socials{left:515px;top:4455px;display:flex;gap:14px}
.social{width:38px;height:38px;border-radius:50%;background:#1d4e8c}
.copyright{left:0;top:4518px;width:1200px;text-align:center;font-size:12px;color:#888}
.copyright b{color:var(--blue);font-weight:500}
</style>
</head>
<body>
<div class="page">

  <!-- header -->
  <div class="abs brand-panel"></div>
  <div class="abs hero-photo" role="img" aria-label="Aerial view of a tropical island with white sand beach and turquoise sea"></div>
  <div class="abs" style="left:366px;top:0;width:834px;height:116px;background:var(--white)"></div>
  <div class="abs brand"><span class="brand-dot"></span>DRIFT US TO HAVEN</div>
  <div class="abs util-nav"><span>CONTACT US</span><span class="sep">|</span><span>BOOK NOW</span></div>
  <nav class="abs main-nav">
    <span class="active">HOME</span><span>DESTINATION</span><span>TOURS</span><span>TAILOR-MADE</span><span>SPECIAL OFFERS</span><span>ABOUT US</span><span>REVIEWS</span>
  </nav>

  <!-- hero -->
  <h1 class="abs hero-title">NEWZEALAND</h1>
  <p class="abs hero-sub">DRIFT US TO HAVEN</p>
  <div class="abs hero-arrows">
    <div class="hero-arrow"><svg width="14" height="20" viewBox="0 0 14 20"><path d="M11 2 3 10l8 8" fill="none" stroke="#222" stroke-width="2.5"/></svg></div>
    <div class="hero-arrow"><svg width="14" height="20" viewBox="0 0 14 20"><path d="M3 2l8 8-8 8" fill="none" stroke="#222" stroke-width="2.5"/></svg></div>
  </div>
  <div class="abs video-disc" role="img" aria-label="Aerial video still of a lagoon and islands">
    <div class="video-label">INTRODUCING NEWZEALAND</div>
    <div class="play"><svg width="22" height="24" viewBox="0 0 22 24"><path d="M4 2l16 10L4 22z" fill="#fff"/></svg></div>
  </div>

  <!-- welcome -->
  <h2 class="abs welcome-title">WELCOME TO<br>DRIFT US TO HAVEN</h2>
  <p class="abs welcome-lede">Lorem Ipsum is simply dummy text of the printing and typesetting industry. Lorem Ipsum has been the industry's standard dummy text ever since the 1500s, when an unknown</p>
  <div class="abs welcome-body">
    <p>Lorem Ipsum is simply dummy text of the printing and typesetting industry. Lorem Ipsum has been the industry's standard dummy text ever since the 1500s, when an unknown printer took a galley of type and scrambled it to make a type specimen book. It has survived not only five centuries, but also the leap into electronic typesetting, remaining essentially unchanged.</p>
    <p>It was popularised in the 1960s with the release of Inkleaf sheets containing Lorem Ipsum passages, and more recently with desktop publishing software like Quillset Layout including versions of Lorem Ipsum.</p>
  </div>

  <!-- included -->
  <div class="abs inc-band"></div>
  <div class="abs ghost-word inc-ghost">INCLUDED?</div>
  <h2 class="abs section-title inc-title">WHAT'S INCLUDED?</h2>
  <ul class="abs inc-list">
    <li><svg width="16" height="16" viewBox="0 0 16 16"><rect x="1" y="1" width="14" height="14" fill="none" stroke="#00a990" stroke-width="1.5"/><path d="M4 8l3 3 5-6" fill="none" stroke="#00a990" stroke-width="1.8"/></svg><span>Return international economy flights, taxes and current fuel surcharges (subject to change)</span></li>
    <li><svg width="16" height="16" viewBox="0 0 16 16"><rect x="1" y="1" width="14" height="14" fill="none" stroke="#00a990" stroke-width="1.5"/><path d="M4 8l3 3 5-6" fill="none" stroke="#00a990" stroke-width="1.8"/></svg><span>Deluxe accommodation</span></li>
    <li><svg width="16" height="16" viewBox="0 0 16 16"><rect x="1" y="1" width="14" height="14" fill="none" stroke="#00a990" stroke-width="1.5"/><path d="M4 8l3 3 5-6" fill="none" stroke="#00a990" stroke-width="1.8"/></svg><span>Exclusive touring and dining experiences</span></li>
    <li><svg width="16" height="16" viewBox="0 0 16 16"><rect x="1" y="1" width="14" height="14" fill="none" stroke="#00a990" stroke-width="1.5"/><path d="M4 8l3 3 5-6" fill="none" stroke="#00a990" stroke-width="1.8"/></svg><span>Sightseeing with the experts</span></li>
    <li><svg width="16" height="16" viewBox="0 0 16 16"><rect x="1" y="1" width="14" height="14" fill="none" stroke="#00a990" stroke-width="1.5"/><path d="M4 8l3 3 5-6" fill="none" stroke="#00a990" stroke-width="1.8"/></svg><span>Expert National Experts and knowledgeable local guides</span></li>
    <li><svg width="16" height="16" viewBox="0 0 16 16"><rect x="1" y="1" width="14" height="14" fill="none" stroke="#00a990" stroke-width="1.5"/><path d="M4 8l3 3 5-6" fill="none" stroke="#00a990" stroke-width="1.8"/></svg><span>Specialist advice from our experienced travel consultants</span></li>
  </ul>
  <div class="abs inc-photo" role="img" aria-label="Aerial view of two small green islands in deep blue sea"></div>

  <!-- tours -->
  <div class="abs ghost-word tours-ghost">TOURS</div>
  <h2 class="abs section-title tours-title">OUR DELUX TOURS</h2>

  <article class="abs tour-card" style="left:76px;top:1807px">
    <div class="tour-photo" role="img" aria-label="Green island under a cloudy sky" style="background:linear-gradient(180deg,#9fb8c9,#e6eef2 40%,#2f6f5a 62%,#0f4f6e)"></div>
    <div class="tour-meta"><div class="tour-name">Lorem Ipsum is simply dummy.</div><div class="tour-facts"><div class="tour-days">16<small>DAYS</small></div><div class="tour-price"><small>FROM</small>$9,780pp</div></div></div>
    <p class="tour-text">Lorem Ipsum is simply dummy text of the printing and typesetting industry. Lorem Ipsum has been the industry's standard dummy text ever since when an unknown.</p>
    <span class="btn tour-btn">VIEW TOUR</span>
  </article>
  <article class="abs tour-card" style="left:440px;top:1807px">
    <div class="tour-photo" role="img" aria-label="Aerial view of a forested island with a sandy beach" style="background:radial-gradient(ellipse at 50% 55%,#3f7a3a 0%,#d7cfa8 28%,#3aa19a 45%,#135a73 100%)"></div>
    <div class="tour-meta"><div class="tour-name">Lorem Ipsum is simply dummy.</div><div class="tour-facts"><div class="tour-days">16<small>DAYS</small></div><div class="tour-price"><small>FROM</small>$9,780pp</div></div></div>
    <p class="tour-text">Lorem Ipsum is simply dummy text of the printing and typesetting industry. Lorem Ipsum has been the industry's standard dummy text ever since when an unknown.</p>
    <span class="btn tour-btn">VIEW TOUR</span>
  </article>
  <article class="abs tour-card" style="left:800px;top:1807px">
    <div class="tour-photo" role="img" aria-label="Limestone islets in a turquoise lagoon" style="background:linear-gradient(135deg,#4d7a52,#2e8f8a 45%,#7ac3bd 70%,#2b6d70)"></div>
    <div class="tour-meta"><div class="tour-name">Lorem Ipsum is simply dummy.</div><div class="tour-facts"><div class="tour-days">16<small>DAYS</small></div><div class="tour-price"><small>FROM</small>$9,780pp</div></div></div>
    <p class="tour-text">Lorem Ipsum is simply dummy text of the printing and typesetting industry. Lorem Ipsum has been the industry's standard dummy text ever since when an unknown.</p>
    <span class="btn tour-btn">VIEW TOUR</span>
  </article>

  <article class="abs tour-card" style="left:76px;top:2473px">
    <div class="tour-photo" role="img" aria-label="Tropical bay with palm trees and islets" style="background:linear-gradient(180deg,#4f93c9,#cfe3f0 35%,#3e6b3a 60%,#1f6f86)"></div>
    <div class="tour-meta"><div class="tour-name">Lorem Ipsum is simply dummy.</div><div class="tour-facts"><div class="tour-days">16<small>DAYS</small></div><div class="tour-price"><small>FROM</small>$9,780pp</div></div></div>
    <p class="tour-text">Lorem Ipsum is simply dummy text of the printing and typesetting industry. Lorem Ipsum has been the industry's standard dummy text ever since when an unknown.</p>
    <span class="btn tour-btn">VIEW TOUR</span>
  </article>
  <article class="abs tour-card" style="left:440px;top:2473px">
    <div class="tour-photo" role="img" aria-label="Aerial view of a pier over clear shallow water" style="background:linear-gradient(160deg,#1a6a8c,#3fb0c4 45%,#dcd5b5 60%,#3d7d4a)"></div>
    <div class="tour-meta"><div class="tour-name">Lorem Ipsum is simply dummy.</div><div class="tour-facts"><div class="tour-days">16<small>DAYS</small></div><div class="tour-price"><small>FROM</small>$9,780pp</div></div></div>
    <p class="tour-text">Lorem Ipsum is simply dummy text of the printing and typesetting industry. Lorem Ipsum has been the industry's standard dummy text ever since when an unknown.</p>
    <span class="btn tour-btn">VIEW TOUR</span>
  </article>
  <article class="abs tour-card" style="left:800px;top:2473px">
    <div class="tour-photo" role="img" aria-label="Coastline with green hills at sunset" style="background:linear-gradient(180deg,#6b8aa6,#2e5a70 40%,#1e5c4c 70%,#104050)"></div>
    <div class="tour-meta"><div class="tour-name">Lorem Ipsum is simply dummy.</div><div class="tour-facts"><div class="tour-days">16<small>DAYS</small></div><div class="tour-price"><small>FROM</small>$9,780pp</div></div></div>
    <p class="tour-text">Lorem Ipsum is simply dummy text of the printing and typesetting industry. Lorem Ipsum has been the industry's standard dummy text ever since when an unknown.</p>
    <span class="btn tour-btn">VIEW TOUR</span>
  </article>

  <span class="abs btn explore-btn">EXPLORE MORE</span>

  <!-- countries -->
  <div class="abs ghost-word countries-ghost">COUNTRIES</div>
  <h2 class="abs section-title countries-title">EXPLORE OUR COUNTRIES</h2>
  <div class="abs tile" role="img" aria-label="New Zealand: aerial view of reef and coastline" style="left:76px;top:3407px;width:513px;height:394px;font-size:34px;background:linear-gradient(135deg,#2c6f7f,#6fb7b8 45%,#c9d5c5 60%,#1d5e6f)">New Zealand</div>
  <div class="abs tile" role="img" aria-label="Vietnam: island surrounded by blue sea" style="left:617px;top:3407px;width:503px;height:174px;font-size:32px;background:radial-gradient(ellipse at 55% 60%,#3f7a3a,#2fa3a0 40%,#176080)">Vietnam</div>
  <div class="abs tile" role="img" aria-label="Indonesia: limestone islets in a lagoon" style="left:617px;top:3615px;width:503px;height:186px;font-size:32px;background:linear-gradient(135deg,#3b6d45,#2c8f8a 50%,#0f4f66)">Indonesia</div>
  <div class="abs tile" role="img" aria-label="Thailand: hilly coastline" style="left:76px;top:3835px;width:242px;height:226px;font-size:26px;background:linear-gradient(180deg,#7fa6bf,#3d6f55 50%,#1a6278)">Thailand</div>
  <div class="abs tile" role="img" aria-label="Malaysia: islands in turquoise water" style="left:345px;top:3835px;width:241px;height:226px;font-size:26px;background:linear-gradient(160deg,#2c7a6a,#4cb4a8 50%,#155c70)">Malaysia</div>
  <div class="abs tile" role="img" aria-label="Vietnam: aerial beach and reef" style="left:614px;top:3835px;width:241px;height:226px;font-size:26px;background:linear-gradient(140deg,#0f3d6a,#2a8fb5 50%,#9ad0c4)">Vietnam</div>
  <div class="abs tile" role="img" aria-label="Thailand: rocky islets in a bay" style="left:882px;top:3835px;width:238px;height:226px;font-size:26px;background:linear-gradient(135deg,#3e6e4e,#3aa9a2 50%,#1b6c82)">Thailand</div>

  <!-- footer -->
  <div class="abs footer-rule"></div>
  <ul class="abs foot-col" style="left:76px"><li>Our Philosophy</li><li>Why Book with Us?</li><li>Price Promise</li><li>Contact Us</li><li>Blog Post</li></ul>
  <ul class="abs foot-col" style="left:293px"><li>Booking Conditions</li><li>Privacy Policy</li><li>Customer Reviews</li><li>FAQ's</li><li>Customer Service</li></ul>
  <ul class="abs foot-col" style="left:507px"><li>China Tours</li><li>Vietnam Tours</li><li>India Tours</li><li>Japan Tours</li><li>Myanmar Tours</li></ul>
  <div class="abs brochures">
    <div class="brochure" role="img" aria-label="Tour brochure cover"></div>
    <div class="brochure" role="img" aria-label="Tour brochure cover"></div>
    <div class="brochure" role="img" aria-label="Tour brochure cover"></div>
    <div class="brochure" role="img" aria-label="Tour brochure cover"></div>
  </div>
  <span class="abs btn brochure-btn">REQUEST A BROCHURE NOW</span>
  <div class="abs socials"><span class="social"></span><span class="social"></span><span class="social" style="background:#c4302b"></span><span class="social"></span></div>
  <p class="abs copyright"><b>DRIFT US TO HAVEN</b>. 2019 . All Rights Reserved.</p>

</div>
</body>
</html>
```